Occupational Therapist does home accessibility for disabled folks; needs business card design

We need a business card for a company in Portland, Oregon that specializes in making homes accessible, comfortable, and functional for people who are disabled or aging who would like to stay in THEIR home. Our medical background as Occupational Therapists allows us to translate the functional needs of the person into the recommendations for the design of the home remodel.

Target Market(s)

Elderly, children of elderly
People with disabilities, families of people with disabilities

Industry/Entity Type

Business

Contact Information for Business Card

Company name: HomeWise
Name: Danielle Reyes Crawford, OTR/L, CAPS, ECHM
Occupational Therapist, Home Modification & Accessibility Specialist
website: www.homewiseforyears.com
email: homewiseforyears@nestmail.example
phone: (503)218-4057
CCB #: 487315

Font styles to use
Sans Serif

Requirements
Must have
• My logo
• Easy to read font with contrasting background
• Please list the Services offered: Occupational Therapy, Home safety & accessibility assessments, Home modification consulting, project management
Nice to have
• Friendly, welcoming feel
Should not have
• Dark colored background

```html
<!DOCTYPE html>
<html lang="en">
<head>
<meta charset="utf-8">
<title>HomeWise Business Card</title>
<link href="https://fonts.googleapis.com/css2?family=Open+Sans:wght@400;600;700&display=swap" rel="stylesheet">
<style>
  :root {
    --backdrop: #d8d3cc;
    --card: #0d0d0d;
    --orange: #e0921f;
    --white: #f2f2f2;
    --grey: #a9a9a9;
  }
  * { margin: 0; padding: 0; box-sizing: border-box; }
  html, body {
    width: 1200px; height: 900px; overflow: hidden;
    background: var(--backdrop);
    font-family: "Open Sans", Arial, sans-serif;
  }
  .stage {
    position: relative; width: 1200px; height: 900px;
    display: flex; justify-content: center; align-items: center; gap: 40px;
  }
  .card {
    position: relative; width: 520px; height: 300px;
    background: var(--card); color: var(--white);
    box-shadow: 0 10px 28px rgba(0,0,0,0.28);
  }
  /* Front */
  .holder {
    position: absolute; left: 34px; top: 36px;
  }
  .holder-name {
    color: var(--orange); font-weight: 700; font-size: 17px; letter-spacing: 0.2px;
  }
  .holder-role {
    margin-top: 6px; font-size: 14px; line-height: 1.3; color: var(--white);
  }
  .brand-front {
    position: absolute; right: 34px; top: 108px;
    display: flex; align-items: center; gap: 10px;
  }
  .brand-mark { width: 22px; height: 22px; background: var(--orange); }
  .brand-name {
    font-size: 36px; font-weight: 600; color: var(--white); letter-spacing: 0.5px;
  }
  .contact {
    position: absolute; left: 34px; bottom: 34px; font-size: 14px;
  }
  .ccb { margin-bottom: 12px; }
  .ccb-label { color: var(--orange); font-weight: 700; }
  .contact-line { display: flex; align-items: center; gap: 10px; line-height: 1.45; }
  .contact-line svg { width: 12px; height: 12px; flex: none; }
  /* Back */
  .card-back {
    display: flex; flex-direction: column; align-items: center; justify-content: center;
    text-align: center;
  }
  .brand-back { display: flex; align-items: center; gap: 12px; }
  .brand-back .brand-mark { background: var(--grey); width: 26px; height: 26px; }
  .brand-back .brand-name { font-size: 44px; color: var(--grey); }
  .services-title { margin-top: 28px; font-weight: 700; font-size: 15px; }
  .services-list { margin-top: 16px; font-size: 13px; line-height: 1.4; color: var(--white); }
</style>
</head>
<body>
<main class="stage">
  <section class="card card-front">
    <div class="holder">
      <p class="holder-name">Danielle Reyes Crawford,OTR/L, CAPS, ECHM</p>
      <p class="holder-role">Occupational Therapist, Home Modification<br>&amp; Accessibility Specialist</p>
    </div>
    <div class="brand-front">
      <span class="brand-mark"></span>
      <span class="brand-name">HomeWise</span>
    </div>
    <div class="contact">
      <p class="ccb"><span class="ccb-label">CCB #:</span> 487315</p>
      <p class="contact-line">
        <svg viewBox="0 0 12 12" aria-hidden="true"><path fill="#e0921f" d="M2.5 1l2 2-1 1.2c.6 1.4 1.8 2.6 3.2 3.2L8 6.5l2 2-1 1.8C5 10 2 7 1.5 2.5z"/></svg>
        (503)218-4057
      </p>
      <p class="contact-line">
        <svg viewBox="0 0 12 12" aria-hidden="true"><rect x="1" y="2.5" width="10" height="7" fill="#e0921f"/><path d="M1 2.5l5 4 5-4" stroke="#0d0d0d" fill="none"/></svg>
        homewiseforyears@nestmail.example
      </p>
      <p class="contact-line">
        <svg viewBox="0 0 12 12" aria-hidden="true"><circle cx="6" cy="6" r="5" fill="#e0921f"/><path d="M1 6h10M6 1c2 2.5 2 7.5 0 10M6 1c-2 2.5-2 7.5 0 10" stroke="#0d0d0d" stroke-width="0.8" fill="none"/></svg>
        www.homewiseforyears.com
      </p>
    </div>
  </section>

  <section class="card card-back">
    <div class="brand-back">
      <span class="brand-mark"></span>
      <span class="brand-name">HomeWise</span>
    </div>
    <p class="services-title">Services offered</p>
    <p class="services-list">Occupational Therapy | Home Safety &amp; Accessibility Assessments,<br>Home Modification Consulting | Project Management</p>
  </section>
</main>
</body>
</html>
```